Business card design for Allied Healthcare provider

We would like a design for front and back of business cards. The design must resonate with all levels of customers from patients, to other health providers and medical. Must also resonate with corporate customers

Target Market(s)

patients, medical practitioners, other health providers and corporate.

Industry/Entity Type

healthcare

Contact Information for Business Card

name, logo, phone and fax numbers, email, website

Requirements
Must have
• not allowing me to change this, but the card must be double sided!! Please take note
Nice to have
• a fresh yet bold design to catch attention.

```html
<!DOCTYPE html>
<html lang="en">
<head>
<meta charset="utf-8">
<title>vitalquay business card</title>
<link rel="stylesheet" href="https://fonts.googleapis.com/css2?family=Rubik:wght@500&family=Raleway:wght@600&family=Roboto:wght@400&display=swap">
<style>
  :root {
    --navy: #1a2c55;
    --amber: #fdb825;
    --white: #ffffff;
    --backdrop: #e0dfe0;
  }
  * { margin: 0; padding: 0; box-sizing: border-box; }
  html, body { width: 1075px; height: 1200px; overflow: hidden; }
  body { background: var(--backdrop); position: relative; }

  .card {
    position: absolute;
    left: 207px;
    width: 660px;
    height: 395px;
    border-radius: 22px;
    overflow: hidden;
  }
  .card--front { top: 189px; background: var(--white); }
  .card--back { top: 638px; background: var(--navy); }

  .wordmark {
    font-family: "Rubik", sans-serif;
    font-weight: 500;
    letter-spacing: -0.5px;
    line-height: 1;
  }
  .card--front .wordmark {
    position: absolute;
    left: 34px;
    top: 72px;
    font-size: 50px;
    color: var(--navy);
  }

  .holder-name {
    position: absolute;
    left: 33px;
    top: 158px;
    font-family: "Raleway", sans-serif;
    font-weight: 600;
    font-size: 29px;
    color: var(--amber);
    line-height: 1.1;
  }
  .holder-role {
    position: absolute;
    left: 33px;
    top: 191px;
    font-family: "Roboto", sans-serif;
    font-size: 18px;
    color: var(--navy);
  }

  .contact-list { position: absolute; left: 31px; top: 243px; list-style: none; }
  .contact-item {
    display: flex;
    align-items: center;
    height: 32px;
    font-family: "Roboto", sans-serif;
    font-size: 18px;
    color: var(--navy);
  }
  .contact-icon { width: 27px; height: 27px; margin-right: 5px; flex: none; }
  .contact-highlight { color: var(--amber); }

  .front-emblem {
    position: absolute;
    left: 374px;
    top: 97px;
    width: 240px;
    height: 240px;
    border-radius: 50%;
    background: var(--amber);
  }

  .back-lockup {
    position: absolute;
    left: 0; right: 0;
    top: 165px;
    display: flex;
    justify-content: center;
    align-items: center;
    gap: 18px;
  }
  .back-dot {
    width: 44px; height: 44px;
    border-radius: 50%;
    background: var(--amber);
    flex: none;
  }
  .card--back .wordmark { font-size: 50px; color: var(--white); }
  .tagline {
    font-family: "Rubik", sans-serif;
    font-weight: 500;
    font-size: 21px;
    color: var(--amber);
    margin-top: 6px;
    letter-spacing: 0.2px;
  }
</style>
</head>
<body>

<section class="card card--front" aria-label="Card front">
  <div class="wordmark">vitalquay</div>
  <div class="holder-name">Marcus Ellery</div>
  <div class="holder-role">Managing Director</div>

  <ul class="contact-list">
    <li class="contact-item">
      <svg class="contact-icon" viewBox="0 0 28 28" aria-hidden="true">
        <circle cx="14" cy="14" r="14" fill="var(--amber)"/>
        <path d="M9.5 7.5c.8-.6 1.6-.4 2 .3l1.3 2.3c.4.7.2 1.4-.4 1.8l-.9.6c.6 1.6 1.8 2.9 3.4 3.6l.6-.9c.4-.6 1.1-.8 1.8-.4l2.3 1.3c.7.4.9 1.2.3 2-1 1.4-2.5 2-4.1 1.4-3.6-1.3-6.2-3.9-7.5-7.5-.6-1.6 0-3.1 1.2-4.5z" fill="var(--white)"/>
      </svg>
      021-555 0148
    </li>
    <li class="contact-item">
      <svg class="contact-icon" viewBox="0 0 28 28" aria-hidden="true">
        <circle cx="14" cy="14" r="14" fill="var(--navy)"/>
        <rect x="9.5" y="6.5" width="9" height="4.5" fill="var(--white)"/>
        <rect x="6.5" y="11.5" width="15" height="7" rx="1.5" fill="var(--white)"/>
        <rect x="9.5" y="16" width="9" height="6" fill="var(--white)" stroke="var(--navy)" stroke-width="1.2"/>
      </svg>
      021-555 0149
    </li>
    <li class="contact-item">
      <svg class="contact-icon" viewBox="0 0 28 28" aria-hidden="true">
        <circle cx="14" cy="14" r="14" fill="var(--amber)"/>
        <rect x="7" y="9" width="14" height="10" rx="1" fill="var(--white)"/>
        <path d="M7.5 9.5l6.5 5 6.5-5" fill="none" stroke="var(--amber)" stroke-width="1.2"/>
      </svg>
      hello@vitalquay.com
    </li>
    <li class="contact-item">
      <svg class="contact-icon" viewBox="0 0 28 28" aria-hidden="true">
        <circle cx="14" cy="14" r="14" fill="var(--navy)"/>
        <g fill="none" stroke="var(--white)" stroke-width="1.3">
          <circle cx="14" cy="14" r="7"/>
          <ellipse cx="14" cy="14" rx="3" ry="7"/>
          <path d="M7 14h14M8 10.5h12M8 17.5h12"/>
        </g>
      </svg>
      www.<span class="contact-highlight">vitalquay</span>.com
    </li>
  </ul>

  <div class="front-emblem" aria-hidden="true"></div>
</section>

<section class="card card--back" aria-label="Card back">
  <div class="back-lockup">
    <div class="back-dot" aria-hidden="true"></div>
    <div class="back-text">
      <div class="wordmark">vitalquay</div>
      <div class="tagline">recovery • support • health</div>
    </div>
  </div>
</section>

</body>
</html>
```